Medical Waste Company with Logo

Need a business card design that targets office managers in the medical community. This card will be the front line for our sales team to market our services to the community. We would like to have email, phone number, website. Please use the logo attached to create a design that we would be proud of.

Target Market(s)

Medical Clients

Industry/Entity Type

Medical Supply

Contact Information for Business Card

Please use logo attached

Colors

Designer to choose colors to be used in the design.

Requirements
Must have
• Our logo (see attached file)
Nice to have
• Maybe a pop of some sort, raised..?

```html
<!DOCTYPE html>
<html lang="en">
<head>
<meta charset="utf-8">
<title>Northpeak Medical Disposal – Business Card</title>
<link href="https://fonts.googleapis.com/css2?family=Open+Sans:wght@400;600;700&display=swap" rel="stylesheet">
<style>
  :root {
    --bg: #e6e7e9;
    --charcoal: #3d3d3f;
    --brand-blue: #1f64b8;
    --paper: #ffffff;
    --ink-light: #ffffff;
  }
  * { margin: 0; padding: 0; box-sizing: border-box; }
  html, body {
    width: 1200px; height: 977px; overflow: hidden;
    background: var(--bg);
    font-family: "Open Sans", sans-serif;
  }
  .business-card {
    position: absolute;
    left: 100px; top: 203px;
    width: 1000px; height: 571px;
    background: var(--paper);
    box-shadow: 0 18px 40px rgba(0,0,0,0.18);
    overflow: hidden;
  }
  .card-shapes { position: absolute; inset: 0; }
  .contact-side {
    position: absolute;
    left: 92px; top: 150px;
    color: var(--ink-light);
  }
  .person-name { font-size: 32px; font-weight: 700; line-height: 1.1; }
  .person-title { font-size: 18px; font-weight: 600; margin-top: 4px; }
  .address { font-size: 17px; line-height: 1.35; margin-top: 28px; margin-left: 26px; }
  .contact-list { list-style: none; margin-top: 26px; margin-left: 26px; }
  .contact-item {
    display: flex; align-items: center; gap: 18px;
    font-size: 17px; line-height: 1.6;
  }
  .contact-icon { width: 14px; height: 14px; fill: var(--ink-light); flex: none; }
  .brand-name {
    position: absolute;
    left: 585px; top: 215px; width: 360px;
    text-align: center;
    color: var(--brand-blue);
    font-size: 34px; font-weight: 600;
    letter-spacing: 1px; line-height: 1.2;
  }
</style>
</head>
<body>
  <div class="business-card">
    <svg class="card-shapes" width="1000" height="571" viewBox="0 0 1000 571" aria-hidden="true">
      <rect class="panel-dark" x="0" y="0" width="482" height="571" fill="var(--charcoal)"/>
      <polygon class="accent-wedge" points="494,0 498,0 544,571 506,571" fill="var(--brand-blue)"/>
    </svg>

    <div class="contact-side">
      <div class="person-name">Dana Whitfield</div>
      <div class="person-title">Medical Manager</div>
      <div class="address">2480 Harbor Lane, Suite 4,<br>Lakeview, ST 54321</div>
      <ul class="contact-list">
        <li class="contact-item">
          <svg class="contact-icon" viewBox="0 0 24 24"><path d="M6.6 10.8a15.1 15.1 0 0 0 6.6 6.6l2.2-2.2c.3-.3.7-.4 1-.2 1.1.4 2.3.6 3.6.6.6 0 1 .4 1 1V20c0 .6-.4 1-1 1C10.6 21 3 13.4 3 4c0-.6.4-1 1-1h3.5c.6 0 1 .4 1 1 0 1.3.2 2.5.6 3.6.1.3 0 .7-.2 1l-2.3 2.2z"/></svg>
          <span>555 012 3478</span>
        </li>
        <li class="contact-item">
          <svg class="contact-icon" viewBox="0 0 24 24"><path d="M2 5h20v14H2z M2 5l10 8 10-8" stroke="var(--charcoal)" stroke-width="1.5"/></svg>
          <span>hello@northpeakmedical.com</span>
        </li>
        <li class="contact-item">
          <svg class="contact-icon" viewBox="0 0 24 24"><circle cx="12" cy="12" r="10"/><path d="M2 12h20M12 2c3 3 3 17 0 20M12 2c-3 3-3 17 0 20" stroke="var(--charcoal)" stroke-width="1.5" fill="none"/></svg>
          <span>www.northpeakmedical.com</span>
        </li>
      </ul>
    </div>

    <div class="brand-name">NORTHPEAK MEDICAL<br>DISPOSAL</div>
  </div>
</body>
</html>
```